KRV In Home Flier

To prepare a flier to be placed directly into existing clients homes, which shares additional services available. These are clients that are using KRV Cleaning services and we want to use our KRV Pest Control or BMO (Bravo Mend On)Maintenance Services

Target Market(s)

residential home owners / Renters

Industry/Entity Type

Property Maintenance

Colors

Designer to choose colors to be used in the design.

Requirements
Must have
• Must be crisp and clean - design should pop - A CLEAR call to action
Nice to have
• See previous designed uploaded
Should not have

```html
<!DOCTYPE html>
<html lang="en">
<head>
<meta charset="utf-8">
<title>KRV In Home Flier</title>
<link href="https://fonts.googleapis.com/css2?family=Nunito:wght@400;600;700;800&family=Oswald:wght@500;600&display=swap" rel="stylesheet">
<style>
  :root{
    --blue:#1f5c99;
    --navy:#173d6b;
    --purple:#7a1d6e;
    --ink:#2a2a2a;
    --stage:#8a8a8a;
    --panel:#eef0f2;
    --white:#ffffff;
  }
  *{box-sizing:border-box;margin:0;padding:0}
  html,body{width:1200px;height:949px;overflow:hidden}
  body{background:var(--stage);font-family:"Nunito",sans-serif;color:var(--ink);position:relative}
  .flyer{position:absolute;top:86px;width:548px;height:776px;background:var(--white);overflow:hidden;box-shadow:0 8px 18px rgba(0,0,0,.35)}
  .flyer--pest{left:38px}
  .flyer--repair{left:614px}
  .hero-photo{position:absolute;left:0;top:60px;width:548px;height:350px}
  .hero-photo--pest{background:linear-gradient(120deg,#5b6570 0%,#2f5ea8 45%,#c9ccd0 85%)}
  .hero-photo--repair{background:linear-gradient(120deg,#4e5257 0%,#a6a39b 45%,#5b6f7e 80%,#3b8a8c 100%)}
  .shapes{position:absolute;left:0;top:0;width:548px;height:776px}
  .brand{position:absolute;left:34px;top:30px;display:flex;align-items:center;gap:8px;font-weight:800;font-size:17px;color:var(--blue)}
  .brand-dot{width:26px;height:26px;border-radius:50%;background:var(--purple)}
  .header-title{position:absolute;right:16px;top:19px;font-weight:800;font-size:22px;color:var(--white);letter-spacing:.3px}
  .perks{position:absolute;left:36px;top:146px;list-style:none;color:var(--white);font-weight:700;font-size:12px;line-height:22px}
  .perks li::before{content:"• "}
  .tagline{position:absolute;left:36px;top:228px;color:var(--white);font-weight:800;font-size:19.5px}
  .section-title{position:absolute;left:49px;font-family:"Oswald",sans-serif;font-weight:600;color:var(--purple);font-size:26px;letter-spacing:-.3px}
  .thumb{position:absolute;width:148px;height:94px;border-radius:6px;box-shadow:0 1px 4px rgba(0,0,0,.3)}
  .service{position:absolute;display:flex;align-items:center;gap:6px;font-weight:700;font-size:14.5px;color:var(--ink)}
  .service svg{width:12px;height:12px}
  .copy{position:absolute;left:45px;width:470px;font-size:13.5px;line-height:18px}
  .copy--strong{font-weight:800}
  .copy--blue{color:var(--blue);font-weight:800}
  .cta{position:absolute;left:24px;top:744px;color:var(--white);font-weight:700;font-size:14.5px}
  .phone{position:absolute;left:304px;top:722px;display:flex;align-items:center;gap:5px;font-weight:800;font-size:28px;color:var(--purple)}
  .phone svg{width:24px;height:24px}
</style>
</head>
<body>

<!-- Pest control flyer -->
<section class="flyer flyer--pest">
  <div class="hero-photo hero-photo--pest" role="img" aria-label="Technician in blue overalls spraying pest treatment along a floor"></div>
  <svg class="shapes" viewBox="0 0 548 776" aria-hidden="true">
    <defs>
      <linearGradient id="bandA" x1="0" x2="1"><stop offset="0" stop-color="#2a6db3"/><stop offset="1" stop-color="#173d6b"/></linearGradient>
      <linearGradient id="panelA" x1="0" y1="0" x2="0" y2="1"><stop offset="0" stop-color="#ffffff"/><stop offset="1" stop-color="#dfe2e6"/></linearGradient>
    </defs>
    <rect x="0" y="0" width="548" height="64" fill="var(--blue)"/>
    <rect x="0" y="62" width="548" height="3" fill="#ffffff"/>
    <path d="M0 0 H258 L230 84 Q225 98 208 98 H0 Z" fill="url(#panelA)"/>
    <rect x="394" y="316" width="32" height="60" fill="var(--navy)"/>
    <path d="M0 346 L169 320 L548 392 L548 400 L169 336 L0 380 Z" fill="url(#bandA)"/>
    <path d="M0 380 L169 336 L548 400" stroke="var(--purple)" stroke-width="3" fill="none"/>
    <path d="M0 384 L169 340 L548 404 V776 H0 Z" fill="#ffffff"/>
    <rect x="0" y="726" width="220" height="4" fill="var(--purple)"/>
    <path d="M0 730 H258 L278 776 H0 Z" fill="url(#bandA)"/>
    <rect x="290" y="764" width="258" height="4" fill="var(--purple)"/>
    <rect x="270" y="768" width="278" height="8" fill="var(--navy)"/>
  </svg>
  <div class="brand"><span class="brand-dot"></span>KRV Pest Control</div>
  <h1 class="header-title">PEST CONTROL SERVICE</h1>
  <ul class="perks">
    <li>EUROPEAN MANAGED</li>
    <li>MONTHLY - QUARTERLY - ANNUALLY MAINTENANCE CONTRACTS</li>
    <li>ON CALL SERVICE</li>
  </ul>
  <p class="tagline">YOUR PROPERTY, OUR PRIORITY.</p>
  <h2 class="section-title" style="top:394px">OUR SERVICES</h2>
  <div class="thumb" style="left:45px;top:438px;background:linear-gradient(135deg,#eceae6,#c9a070)" role="img" aria-label="Worker in protective suit treating a floor"></div>
  <div class="thumb" style="left:201px;top:438px;background:linear-gradient(135deg,#c9c3a8,#6d5f45)" role="img" aria-label="Spray hose treating soil by a house wall"></div>
  <div class="thumb" style="left:357px;top:438px;background:linear-gradient(135deg,#8a6e55,#e6e2dc)" role="img" aria-label="Technician inspecting a kitchen with the home owner"></div>
  <div class="service" style="left:45px;top:550px"><svg viewBox="0 0 12 12"><circle cx="6" cy="6" r="5" fill="none" stroke="var(--purple)" stroke-width="1.2"/><path d="M3.5 6 L5.3 7.8 L9 3.8" fill="none" stroke="var(--purple)" stroke-width="1.3"/></svg>General Pest Control</div>
  <div class="service" style="left:241px;top:550px"><svg viewBox="0 0 12 12"><circle cx="6" cy="6" r="5" fill="none" stroke="var(--purple)" stroke-width="1.2"/><path d="M3.5 6 L5.3 7.8 L9 3.8" fill="none" stroke="var(--purple)" stroke-width="1.3"/></svg>Bed Bugs Control</div>
  <div class="service" style="left:410px;top:550px"><svg viewBox="0 0 12 12"><circle cx="6" cy="6" r="5" fill="none" stroke="var(--purple)" stroke-width="1.2"/><path d="M3.5 6 L5.3 7.8 L9 3.8" fill="none" stroke="var(--purple)" stroke-width="1.3"/></svg>Rat Control</div>
  <div class="service" style="left:45px;top:578px"><svg viewBox="0 0 12 12"><circle cx="6" cy="6" r="5" fill="none" stroke="var(--purple)" stroke-width="1.2"/><path d="M3.5 6 L5.3 7.8 L9 3.8" fill="none" stroke="var(--purple)" stroke-width="1.3"/></svg>Cockroaches Control</div>
  <div class="service" style="left:241px;top:578px"><svg viewBox="0 0 12 12"><circle cx="6" cy="6" r="5" fill="none" stroke="var(--purple)" stroke-width="1.2"/><path d="M3.5 6 L5.3 7.8 L9 3.8" fill="none" stroke="var(--purple)" stroke-width="1.3"/></svg>Ant Control</div>
  <p class="copy" style="top:617px">KRV Pest Control is reinventing the pest control service industry in Dubai.</p>
  <p class="copy copy--blue" style="top:646px">This means you get the right Pest Control Workers, with the right tools at the right time!</p>
  <p class="cta">Call us now for a free estimate!</p>
  <div class="phone"><svg viewBox="0 0 24 24"><circle cx="12" cy="12" r="10.5" fill="none" stroke="var(--ink)" stroke-width="1.6"/><path d="M8.2 6.5 L10 6.2 L11 9 L9.8 10 Q10.8 12.6 13.8 14.2 L14.9 13 L17.6 14.1 L17.3 15.9 Q16 17.4 13.8 16.6 Q8.6 14.4 7.2 9.6 Q6.8 7.6 8.2 6.5 Z" fill="var(--ink)"/></svg>800 BRIGHTLY</div>
</section>

<!-- Home maintenance flyer -->
<section class="flyer flyer--repair">
  <div class="hero-photo hero-photo--repair" role="img" aria-label="Bright living room with a smiling maintenance staff member in uniform"></div>
  <svg class="shapes" viewBox="0 0 548 776" aria-hidden="true">
    <defs>
      <linearGradient id="bandB" x1="0" x2="1"><stop offset="0" stop-color="#2a6db3"/><stop offset="1" stop-color="#173d6b"/></linearGradient>
      <linearGradient id="panelB" x1="0" y1="0" x2="0" y2="1"><stop offset="0" stop-color="#ffffff"/><stop offset="1" stop-color="#dfe2e6"/></linearGradient>
    </defs>
    <rect x="0" y="0" width="548" height="64" fill="var(--blue)"/>
    <rect x="0" y="62" width="548" height="3" fill="#ffffff"/>
    <path d="M0 0 H254 L228 84 Q223 98 206 98 H0 Z" fill="url(#panelB)"/>
    <rect x="394" y="316" width="32" height="60" fill="var(--navy)"/>
    <path d="M0 346 L169 320 L548 392 L548 400 L169 336 L0 380 Z" fill="url(#bandB)"/>
    <path d="M0 380 L169 336 L548 400" stroke="var(--purple)" stroke-width="3" fill="none"/>
    <path d="M0 384 L169 340 L548 404 V776 H0 Z" fill="#ffffff"/>
    <rect x="0" y="726" width="220" height="4" fill="var(--purple)"/>
    <path d="M0 730 H258 L278 776 H0 Z" fill="url(#bandB)"/>
    <rect x="290" y="764" width="258" height="4" fill="var(--purple)"/>
    <rect x="270" y="768" width="278" height="8" fill="var(--navy)"/>
  </svg>
  <div class="brand" style="left:40px"><span class="brand-dot"></span>Bravo Mend On</div>
  <h1 class="header-title">HOME MAINTENANCE</h1>
  <ul class="perks">
    <li>EUROPEAN MANAGED</li>
    <li>ANNUALLY MAINTENANCE CONTRACTS</li>
    <li>ON CALL SERVICE</li>
  </ul>
  <p class="tagline">YOUR PROPERTY, OUR PRIORITY.</p>
  <p class="copy" style="top:400px;font-size:13px">Bravo Mend On is reinventing the maintenance industry in Dubai with GPS technology and world class inventory management.</p>
  <p class="copy copy--strong" style="top:443px;font-size:13.5px">This means you get the right techician, with the right tools at the right time!</p>
  <div class="thumb" style="left:45px;top:496px;background:linear-gradient(135deg,#e4e6e3,#7a8a84)" role="img" aria-label="Technician servicing a wall air conditioner"></div>
  <div class="thumb" style="left:201px;top:496px;background:linear-gradient(135deg,#b33a2e,#3b6fb0)" role="img" aria-label="Electrician testing a wiring panel"></div>
  <div class="thumb" style="left:357px;top:496px;background:linear-gradient(135deg,#d9d4d8,#6e6a6c)" role="img" aria-label="Plumber fitting a chrome sink pipe"></div>
  <h2 class="section-title" style="top:606px;left:47px;font-size:27px">24 HOUR EMERGENCY SERVICES</h2>
  <div class="service" style="left:45px;top:648px"><svg viewBox="0 0 12 12"><circle cx="6" cy="6" r="5" fill="none" stroke="var(--purple)" stroke-width="1.2"/><path d="M3.5 6 L5.3 7.8 L9 3.8" fill="none" stroke="var(--purple)" stroke-width="1.3"/></svg>AC Services</div>
  <div class="service" style="left:242px;top:648px"><svg viewBox="0 0 12 12"><circle cx="6" cy="6" r="5" fill="none" stroke="var(--purple)" stroke-width="1.2"/><path d="M3.5 6 L5.3 7.8 L9 3.8" fill="none" stroke="var(--purple)" stroke-width="1.3"/></svg>Electrical Services</div>
  <div class="service" style="left:45px;top:676px"><svg viewBox="0 0 12 12"><circle cx="6" cy="6" r="5" fill="none" stroke="var(--purple)" stroke-width="1.2"/><path d="M3.5 6 L5.3 7.8 L9 3.8" fill="none" stroke="var(--purple)" stroke-width="1.3"/></svg>Plumbing Services</div>
  <div class="service" style="left:242px;top:676px"><svg viewBox="0 0 12 12"><circle cx="6" cy="6" r="5" fill="none" stroke="var(--purple)" stroke-width="1.2"/><path d="M3.5 6 L5.3 7.8 L9 3.8" fill="none" stroke="var(--purple)" stroke-width="1.3"/></svg>Handyman Services</div>
  <p class="cta">Call us now for a free estimate!</p>
  <div class="phone"><svg viewBox="0 0 24 24"><circle cx="12" cy="12" r="10.5" fill="none" stroke="var(--ink)" stroke-width="1.6"/><path d="M8.2 6.5 L10 6.2 L11 9 L9.8 10 Q10.8 12.6 13.8 14.2 L14.9 13 L17.6 14.1 L17.3 15.9 Q16 17.4 13.8 16.6 Q8.6 14.4 7.2 9.6 Q6.8 7.6 8.2 6.5 Z" fill="var(--ink)"/></svg>800 BRIGHTLY</div>
</section>

</body>
</html>
```